Specialty Contact lens for children

We need a large size canvas 24x36" to advertise specialty fit contact lens for children to control myopia. please visit our website for more about our office theme www.tandriloo.com
We want modern , fresh, happy design. Color blue, green, white. Final design should communicate the best lens choice for the children. Banner to include a picture of happy teen playing sports or out in park without glasses. To portray the new ability to see without glasses.
ORTHO-K #1 MYOPIA control treatment for children
- Corrects your vision while you sleep
- Creates crisp clear vision all day
- Freedom: No glasses, No Surgery, No soft lenses
-Safe and effective for children and adults

Target Market(s)

8-25 years old

Industry/Entity Type

Health Care

Font styles to use
Sans Serif

Colors
0692cd
cee9f5
ecf7fb
ffffff
86cfc6

Requirements
Must have
• Picture of teen playing sports or outdoors without glasses
Nice to have
• office logo on banner. happy color blue, green, white.
• Modern font: century gothic

```html
<!DOCTYPE html>
<html lang="en">
<head>
<meta charset="utf-8">
<title>Ortho-K Myopia Control Poster</title>
<link rel="stylesheet" href="https://fonts.googleapis.com/css2?family=Oswald:wght@700&family=Roboto+Condensed:wght@400&family=Questrial&display=swap">
<style>
  :root {
    --teal: #7fcdc3;
    --teal-deep: #68b8ad;
    --teal-light: #8fdcd2;
    --sky: #cfe6f3;
    --sun: #fddf84;
    --white: #ffffff;
    --ink: #5a5f63;
    --ring: #cfe6f3;
  }
  html, body {
    margin: 0;
    padding: 0;
    width: 864px;
    height: 1200px;
    overflow: hidden;
    background: #d6d6d6;
  }
  .poster {
    position: relative;
    width: 864px;
    height: 1200px;
    overflow: hidden;
    background: radial-gradient(ellipse at 60% 30%, var(--teal-light) 0%, var(--teal) 45%, var(--teal-deep) 100%);
  }
  .backdrop {
    position: absolute;
    inset: 0;
  }
  .headline {
    position: absolute;
    left: 34px;
    top: 58px;
    margin: 0;
    font-family: "Oswald", "Arial Narrow", sans-serif;
    font-weight: 700;
    color: var(--sun);
    line-height: 1.0;
    letter-spacing: -0.5px;
  }
  .headline .line-one { display: block; font-size: 58px; }
  .headline .line-two { display: block; font-size: 58px; margin-top: 2px; }
  .lens-photo {
    position: absolute;
    left: 30px;
    top: 205px;
    width: 228px;
    height: 228px;
    border-radius: 50%;
    border: 4px solid var(--ring);
    background: radial-gradient(circle at 50% 35%, #e8b68f 0%, #b7784f 45%, #4e3a2c 100%);
  }
  .benefits {
    position: absolute;
    left: 298px;
    top: 246px;
    margin: 0;
    padding: 0;
    list-style: none;
    font-family: "Roboto Condensed", "Arial Narrow", sans-serif;
    font-size: 21px;
    color: var(--white);
  }
  .benefits li {
    display: flex;
    align-items: center;
    height: 35.5px;
  }
  .benefits svg {
    width: 14px;
    height: 14px;
    margin-right: 9px;
    flex: none;
  }
  .kid-photo {
    position: absolute;
    left: 350px;
    top: 450px;
    width: 514px;
    height: 750px;
    border-radius: 220px 0 0 0;
    background:
      linear-gradient(180deg, #c98a63 0%, #d8a07c 18%, #d9463f 32%, #c8302e 60%, #3f5c7d 78%, #2f4561 100%);
  }
  .brand {
    position: absolute;
    left: 56px;
    top: 940px;
    width: 320px;
    text-align: center;
    font-family: "Questrial", "Century Gothic", sans-serif;
    font-weight: 400;
    color: var(--ink);
    line-height: 1.05;
  }
  .brand .name { display: block; font-size: 46px; letter-spacing: 1px; }
  .brand .trade { display: block; font-size: 36px; letter-spacing: 3px; }
</style>
</head>
<body>
  <main class="poster">
    <svg class="backdrop" width="864" height="1200" viewBox="0 0 864 1200" aria-hidden="true">
      <polygon class="corner-accent" points="626,0 864,0 864,105" fill="var(--sun)"/>
      <path class="sky-panel" d="M0,570 Q120,505 248,475 L864,650 L864,1200 L410,1200 L0,1075 Z" fill="var(--sky)"/>
      <path class="sky-edge" d="M248,475 L864,650 L864,635 L262,470 Z" fill="var(--teal-light)"/>
    </svg>

    <h1 class="headline">
      <span class="line-one">ORTHO-K #1 MYOPIA</span>
      <span class="line-two">control treatment for children</span>
    </h1>

    <div class="lens-photo" role="img" aria-label="Photo of a smiling woman holding a contact lens on her fingertip and a pair of glasses"></div>

    <ul class="benefits">
      <li><svg viewBox="0 0 14 14"><path d="M2 7.5 L5.5 11 L12 3" fill="none" stroke="#fddf84" stroke-width="2.4" stroke-linecap="round" stroke-linejoin="round"/></svg>Corrects your vision while you sleep</li>
      <li><svg viewBox="0 0 14 14"><path d="M2 7.5 L5.5 11 L12 3" fill="none" stroke="#fddf84" stroke-width="2.4" stroke-linecap="round" stroke-linejoin="round"/></svg>Creates crisp clear vision all day</li>
      <li><svg viewBox="0 0 14 14"><path d="M2 7.5 L5.5 11 L12 3" fill="none" stroke="#fddf84" stroke-width="2.4" stroke-linecap="round" stroke-linejoin="round"/></svg>Freedom: No glasses, No Surgery, No soft lenses</li>
      <li><svg viewBox="0 0 14 14"><path d="M2 7.5 L5.5 11 L12 3" fill="none" stroke="#fddf84" stroke-width="2.4" stroke-linecap="round" stroke-linejoin="round"/></svg>Safe and effective for children and adults</li>
    </ul>

    <div class="kid-photo" role="img" aria-label="Photo of an excited boy in a red t-shirt and denim shorts playing a video game with a controller, without glasses"></div>

    <div class="brand">
      <span class="name">TANDRILOO</span>
      <span class="trade">OPTOMETRY</span>
    </div>
  </main>
</body>
</html>
```